Up to the Challenge - PPT Template with Splash Slide

We are looking for a PPT template that has 4 slides.
1. Splash slide (Creative, fun, no content, a visual representation of the theme)
2. Section header slide
3. Content Slide
4. Content Slide, another design option
The theme is 'UP to the Challenge'. The design should reflect this theme.
The colors should be in Purple (#864B99), Blue (#0A80C2), and Green (#52B054).

```html
<!DOCTYPE html>
<html lang="en">
<head>
<meta charset="utf-8">
<title>Up to the Challenge – Global Summit Template</title>
<link href="https://fonts.googleapis.com/css2?family=Merriweather:wght@700;900&family=Montserrat:wght@400;500;600;700&display=swap" rel="stylesheet">
<style>
:root{
  --purple:#864B99;
  --blue:#0A80C2;
  --green:#52B054;
  --ink:#231f20;
  --grey:#6d6e71;
  --backdrop:#e3e4e6;
  --white:#ffffff;
  --serif:"Merriweather", Georgia, serif;
  --sans:"Montserrat", Arial, sans-serif;
}
*{margin:0;padding:0;box-sizing:border-box}
html,body{width:1200px;height:3267px;overflow:hidden}
body{background:var(--backdrop);position:relative;font-family:var(--sans);color:var(--ink)}
.slide{position:absolute;left:184px;width:831px;height:468px;background:var(--white);overflow:hidden;box-shadow:0 6px 14px rgba(0,0,0,.18)}
.abs{position:absolute}
.photo{position:absolute}
.tri-bars{position:absolute;display:flex;gap:8px}
.tri-bars span{display:block;height:100%}
.tri-bars span:nth-child(1){background:var(--purple)}
.tri-bars span:nth-child(2){background:var(--green)}
.tri-bars span:nth-child(3){background:var(--blue)}
.footer{position:absolute;left:16px;right:16px;top:434px;height:14px;display:flex;align-items:center;gap:6px}
.footer .site{font-size:9px;letter-spacing:1.6px;font-weight:600}
.footer .rule{flex:1;height:1px;background:var(--blue);opacity:.6}
.footer .copy{font-size:5px;font-weight:500}
.footer .page{width:14px;height:12px;background:var(--purple);color:#fff;font-size:8px;font-weight:700;display:flex;align-items:center;justify-content:center}
.heading{font-family:var(--serif);font-weight:900;color:var(--ink)}
.lorem{font-size:9px;line-height:1.3;color:var(--grey)}

/* slide 1 */
.s1{top:137px}
.s1 .bg{inset:0;background:radial-gradient(ellipse at 72% 45%,#3ab6a0 0%,#2a6fc9 25%,#2b2aa0 48%,#140f58 70%,#07082a 100%)}
.s1 .accent{position:absolute;left:70px;width:7px}
.s1 .kicker{left:91px;top:148px;font-family:var(--serif);font-weight:900;color:#fff;font-size:26px}
.s1 .title{left:91px;top:180px;font-family:var(--serif);font-weight:900;color:#fff;font-size:62px;line-height:1}
.s1 .sub{left:91px;top:262px;font-family:var(--serif);font-weight:900;color:#fff;font-size:41px}
.s1 .date{left:72px;top:403px;color:#fff;font-size:17px;font-weight:700}

/* slide 2 */
.s2{top:644px}
.s2 .heading{left:165px;top:44px;font-size:36px}
.s2 .photo{left:77px;top:109px;width:309px;height:249px;background:linear-gradient(135deg,#9fb7cf,#5c7ea2 50%,#c9d7e4)}
.agenda{position:absolute;left:447px;top:112px;width:300px;list-style:none}
.agenda li{height:68px}
.agenda h3{font-size:15px;font-weight:600}
.agenda p{font-size:8.5px;line-height:1.25;color:var(--grey);padding-left:19px;margin-top:4px}
.agenda li:nth-child(odd) h3{color:var(--blue)}
.agenda li:nth-child(2) h3{color:var(--green)}
.agenda li:nth-child(3) h3{color:var(--purple)}

/* slide 3 */
.s3{top:1154px}
.s3 .heading{left:47px;top:30px;font-size:30px;line-height:1.25}
.s3 .body{left:47px;top:185px;width:212px;text-align:justify}
.s3 .body p{margin-bottom:10px}
.s3 .photo{left:287px;top:0;width:544px;height:264px;background:linear-gradient(90deg,#b9c8d6,#e7ecf1 50%,#c9a98a 70%,#e1e6ea)}
.card{position:absolute;top:185px;width:165px;height:206px;background:var(--blue);box-shadow:0 3px 6px rgba(0,0,0,.2)}
.card h4{height:60px;background:var(--green);color:#fff;font-size:26px;font-weight:600;display:flex;align-items:center;justify-content:center}
.card p{color:#fff;font-size:8.3px;line-height:1.2;padding:10px 14px 0}

/* slide 4 */
.s4{top:1659px}
.s4 .heading{left:37px;top:24px;font-size:24px}
.hub{position:absolute;left:88px;top:134px;width:202px;height:202px;border-radius:50%;background:var(--ink);display:flex;align-items:center;justify-content:center}
.hub .ring{width:186px;height:186px;border-radius:50%;border:2px solid var(--green);background:#fff;display:flex;align-items:center;justify-content:center;text-align:center;font-family:var(--serif);font-weight:900;font-size:29px;line-height:1.15}
.project{position:absolute;left:500px;width:260px}
.project h4{font-size:15px;font-weight:600}
.project p{font-size:9px;line-height:1.25;color:var(--grey);margin-top:3px}
.badge{position:absolute;left:413px;width:64px;height:64px;border-radius:50%}

/* slide 5 */
.s5{top:2158px}
.s5 .photo{left:0;top:36px;width:831px;height:189px;background:linear-gradient(90deg,#1aa0e0,#6a7be6 30%,#c48be0 45%,#35507a 65%,#1f3456 80%,#2fae5e)}
.panel{position:absolute;left:68px;top:147px;width:211px;height:261px;background:var(--ink);color:#fff;padding:20px 18px}
.panel h2{font-family:var(--serif);font-weight:900;font-size:29px}
.panel p{font-size:10.5px;line-height:1.25;margin-top:10px}
.point{position:absolute;width:180px;padding-left:29px}
.point::before{content:"";position:absolute;left:0;top:4px;width:14px;height:14px;border-radius:50%;background:var(--blue)}
.point h4{color:var(--purple);font-size:15px;font-weight:700}
.point p{font-size:8.3px;line-height:1.25;color:var(--grey);margin-top:2px}

/* slide 6 */
.s6{top:2663px}
.thanks{position:absolute;right:484px;top:150px;text-align:right;font-family:var(--serif);font-weight:900;font-size:72px;line-height:1.2;color:#333}
.s6 .photo{left:381px;top:139px;width:276px;height:212px;background:linear-gradient(135deg,#0d2746,#3b6f9c 55%,#b9cfe0)}
.vert-site{position:absolute;left:668px;top:139px;width:39px;height:212px;background:var(--green);display:flex;align-items:center;justify-content:center}
.vert-site span{transform:rotate(-90deg);white-space:nowrap;color:#fff;font-size:14px;font-weight:600;letter-spacing:2px}
.stripe{position:absolute;left:0;bottom:0;width:100%;height:10px;background:repeating-linear-gradient(90deg,var(--purple) 0 52px,#fff 52px 59px,var(--green) 59px 111px,#fff 111px 118px,var(--blue) 118px 170px,#fff 170px 177px)}
</style>
</head>
<body>

<section class="slide s1">
  <div class="photo bg" role="img" aria-label="Digital globe with glowing data grid in blue, purple and green"></div>
  <span class="accent" style="top:155px;height:44px;background:var(--purple)"></span>
  <span class="accent" style="top:203px;height:54px;background:var(--green)"></span>
  <span class="accent" style="top:262px;height:48px;background:var(--blue)"></span>
  <p class="abs kicker">Up to the</p>
  <h1 class="abs title">Challenge ?</h1>
  <p class="abs sub">Global Summit</p>
  <p class="abs date">30th June 2024</p>
</section>

<section class="slide s2">
  <h2 class="abs heading">Agenda</h2>
  <div class="tri-bars" style="left:144px;top:103px;height:11px"><span style="width:53px"></span><span style="width:55px"></span><span style="width:52px"></span></div>
  <div class="photo" role="img" aria-label="Hands holding a tablet with a digital globe over a city skyline"></div>
  <ol class="agenda">
    <li><h3>1. Lorem ipsum</h3><p>Lorem ipsum dolor sit amet, consectetuer adipiscing elit, sed diam nonummy nibh euismod tincid</p></li>
    <li><h3>2. Lorem ipsum</h3><p>Lorem ipsum dolor sit amet, consectetuer adipiscing elit, sed diam nonummy nibh euismod tincid</p></li>
    <li><h3>3. Lorem ipsum</h3><p>Lorem ipsum dolor sit amet, consectetuer adipiscing elit, sed diam nonummy nibh euismod tincid</p></li>
    <li><h3>4. Lorem ipsum</h3><p>Lorem ipsum dolor sit amet, consectetuer adipiscing elit, sed diam nonummy nibh euismod tincid</p></li>
  </ol>
  <div class="footer"><span class="site">website.com</span><span class="rule"></span><span class="copy">Copyright © 2024 Company name. All rights reserved.</span><span class="page">2</span></div>
</section>

<section class="slide s3">
  <h2 class="abs heading">Lorem Ipsum<br>Dolor Sit<br>Ametkeeper.</h2>
  <div class="tri-bars" style="left:47px;top:157px;height:5px"><span style="width:28px"></span><span style="width:30px"></span><span style="width:28px"></span></div>
  <div class="abs body lorem">
    <p>Lorem ipsum dolor sit amet, consectetuer adipiscing elit, sed diam nonummy nibh euismod tincidunt ut laoreet dolore magna aliquam erat volutpat.</p>
    <p>Ut wisi enim ad minim veniam, quis nostrud exerci tation ullamcorper suscipit lobortis nisl ut aliquip ex ea commodo consequat. Duis autem vel eum iriure dolor in hendrerit in vulputate velit esse molestie consequat,</p>
    <p>vel illum dolore eu feugiat nulla facilisis at vero eros et accumsan et iusto odio dignissim qui blandit praesent luptatum zzril delenit augue duis dolore te feugait</p>
  </div>
  <div class="photo" role="img" aria-label="Business team standing before a bright world map backdrop"></div>
  <div class="card" style="left:377px"><h4>Text Here</h4><p>Lorem ipsum dolor sit amet, consectetuer adipiscing elit, sed diam nonummy nibh euismod tincidunt ut laoreet dolore magna aliquam erat volutpat.</p><p>Ut wisi enim ad minim veniam, quis nostrud exerci tation ullamcorper suscipit lobortis nisl ut aliquip ex ea commodo conse</p></div>
  <div class="card" style="left:585px"><h4>Text Here</h4><p>Lorem ipsum dolor sit amet, consectetuer adipiscing elit, sed diam nonummy nibh euismod tincidunt ut laoreet dolore magna aliquam erat volutpat.</p><p>Ut wisi enim ad minim veniam, quis nostrud exerci tation ullamcorper suscipit lobortis nisl ut aliquip ex ea commodo conse</p></div>
  <div class="footer"><span class="site">website.com</span><span class="rule"></span><span class="copy">Copyright © 2024 Company name. All rights reserved.</span><span class="page">3</span></div>
</section>

<section class="slide s4">
  <h2 class="abs heading">Text Added Here</h2>
  <div class="tri-bars" style="left:37px;top:64px;height:5px"><span style="width:28px"></span><span style="width:30px"></span><span style="width:28px"></span></div>
  <div class="hub"><div class="ring">Added<br>Text</div></div>
  <svg class="abs" style="left:0;top:0" width="831" height="468" viewBox="0 0 831 468">
    <g fill="none" stroke="#231f20" stroke-width="1.3">
      <polyline points="294,178 327,129 396,129"/>
      <line x1="311" y1="233" x2="396" y2="233"/>
      <polyline points="294,294 327,341 396,341"/>
    </g>
    <g fill="none" stroke="#fff" stroke-width="2">
      <g transform="translate(445,129)"><circle r="14"/><circle r="8"/><circle r="2.5"/><line x1="0" y1="0" x2="16" y2="-10"/></g>
      <g transform="translate(445,233)"><circle r="14"/><circle r="8"/><circle r="2.5"/><line x1="0" y1="0" x2="16" y2="-10"/></g>
      <g transform="translate(445,339)"><circle r="14"/><circle r="8"/><circle r="2.5"/><line x1="0" y1="0" x2="16" y2="-10"/></g>
    </g>
  </svg>
  <span class="badge" style="top:97px;background:var(--purple);z-index:-0"></span>
  <span class="badge" style="top:201px;background:var(--green)"></span>
  <span class="badge" style="top:307px;background:var(--blue)"></span>
  <svg class="abs" style="left:0;top:0" width="831" height="468" viewBox="0 0 831 468">
    <g fill="none" stroke="#fff" stroke-width="2">
      <g transform="translate(445,129)"><circle r="14"/><circle r="8"/><circle r="2.5"/><line x1="0" y1="0" x2="16" y2="-10"/></g>
      <g transform="translate(445,233)"><circle r="14"/><circle r="8"/><circle r="2.5"/><line x1="0" y1="0" x2="16" y2="-10"/></g>
      <g transform="translate(445,339)"><circle r="14"/><circle r="8"/><circle r="2.5"/><line x1="0" y1="0" x2="16" y2="-10"/></g>
    </g>
  </svg>
  <div class="project" style="top:98px"><h4>Project name</h4><p>Lorem ipsum dolor sit amet, nec an dictas equidem appellantur, ut has commune accommodare. Mea illum, ludus solet idpro.</p></div>
  <div class="project" style="top:203px"><h4>Project name</h4><p>Lorem ipsum dolor sit amet, nec an dictas equidem appellantur, ut has commune accommodare. Mea illum, ludus solet idpro.</p></div>
  <div class="project" style="top:312px"><h4>Project name</h4><p>Lorem ipsum dolor sit amet, nec an dictas equidem appellantur, ut has commune accommodare. Mea illum, ludus solet idpro.</p></div>
  <div class="footer"><span class="site">website.com</span><span class="rule"></span><span class="copy">Copyright © 2024 Company name. All rights reserved.</span><span class="page">4</span></div>
</section>

<section class="slide s5">
  <div class="photo" role="img" aria-label="Hand using a tablet over glowing financial market figures"></div>
  <div class="panel">
    <h2>Text Here</h2>
    <div class="tri-bars" style="position:relative;height:5px;margin-top:8px"><span style="width:28px"></span><span style="width:30px"></span><span style="width:28px"></span></div>
    <p>Lorem ipsum dolor sit amet, consectetuer adipiscing elit, sed diam nonummy nibh euismod tincidunt ut laoreet dolore magna aliquam erat volutpat.</p>
    <p>Ut wisi enim ad minim veniam, quis nostrud exerci tation ullamcorper suscipit lobortis nisl ut aliquip ex ea commodo conse</p>
  </div>
  <div class="point" style="left:321px;top:254px"><h4>Lorem ipsum</h4><p>Lorem ipsum dolor sit amet, consectetuer adipiscing elit, sed diam nonummy nibh euismod tincidunt ut laoreet</p></div>
  <div class="point" style="left:551px;top:254px"><h4>Lorem ipsum</h4><p>Lorem ipsum dolor sit amet, consectetuer adipiscing elit, sed diam nonummy nibh euismod tincidunt ut laoreet</p></div>
  <div class="point" style="left:321px;top:345px"><h4>Lorem ipsum</h4><p>Lorem ipsum dolor sit amet, consectetuer adipiscing elit, sed diam nonummy nibh euismod tincidunt ut laoreet</p></div>
  <div class="point" style="left:551px;top:345px"><h4>Lorem ipsum</h4><p>Lorem ipsum dolor sit amet, consectetuer adipiscing elit, sed diam nonummy nibh euismod tincidunt ut laoreet</p></div>
  <div class="footer"><span class="site">website.com</span><span class="rule"></span><span class="copy">Copyright © 2024 Company name. All rights reserved.</span><span class="page">5</span></div>
</section>

<section class="slide s6">
  <h2 class="thanks">Thank<br>You</h2>
  <div class="photo" role="img" aria-label="Business person behind a world map with travel and finance icons"></div>
  <div class="vert-site"><span>www.website.com</span></div>
  <div class="stripe"></div>
</section>

</body>
</html>
```